Cover Design for my E-Book

I'm looking for cover art for my new book project. It's a business book for musicians entering the field of music for advertising. While it's a business book, the tone of the book is casual, easy to understand and tongue in cheek and I am looking for a design that is simple, clean and modern. I would use the following book covers as references of styles that I think convey the right feeling:

Refold
The Shape Of Routine
Nimble
Upturn by Dominic Falk
Ethical Drift by Gareth Amble

While this direction is a general guide, I am open to being surprised by something very different from the above. I am a musician who worked with creative briefs all the time and I know how maddening they can be to read. I am only now learning how maddening they can be to write. thanks for your help.

Target Market(s)

Music business students, composers and bands

Industry/Entity Type

Business

Requirements
Must have
• Book Title:

Scoring UP - Winning Through The New Age Of Jingle Work

My Name:

Marco Vandesteen

```html
<!DOCTYPE html>
<html lang="en">
<head>
<meta charset="utf-8">
<title>Scoring UP – Marco Vandesteen</title>
<link rel="stylesheet" href="https://fonts.googleapis.com/css2?family=Squada+One&family=Cinzel:wght@400;500&display=swap">
<style>
  :root {
    --page: #ffffff;
    --cover: #000000;
    --ink: #ffffff;
    --eq-magenta: #e0128a;
    --eq-violet: #b21ee6;
    --eq-blue: #2a2cf0;
    --eq-sky: #5aa8f0;
    --eq-mint: #7de8c0;
    --eq-green: #8cf05a;
    --eq-yellow: #f2ec3c;
    --eq-orange: #f07a1e;
  }
  * { margin: 0; padding: 0; box-sizing: border-box; }
  html, body {
    width: 1000px;
    height: 1200px;
    overflow: hidden;
    background: var(--page);
  }
  .book-cover {
    position: absolute;
    left: 152px;
    top: 56px;
    width: 731px;
    height: 1096px;
    background: var(--cover);
    overflow: hidden;
  }
  .cover-type {
    position: absolute;
    inset: 0;
    width: 731px;
    height: 1096px;
  }
  .title {
    font-family: "Squada One", "Arial Narrow", sans-serif;
    fill: var(--ink);
  }
  .subtitle {
    font-family: "Squada One", "Arial Narrow", sans-serif;
    fill: var(--ink);
  }
  .author {
    font-family: "Cinzel", Georgia, serif;
    font-weight: 500;
    fill: var(--ink);
  }
  .equalizer {
    position: absolute;
    left: 0;
    top: 488px;
    width: 731px;
    height: 400px;
    background:
      linear-gradient(to bottom, var(--cover) 0%, rgba(0,0,0,0.55) 30%, rgba(0,0,0,0) 62%, rgba(0,0,0,0) 72%, rgba(0,0,0,0.55) 80%, var(--cover) 100%),
      linear-gradient(to right, var(--eq-magenta) 0%, var(--eq-violet) 16%, var(--eq-blue) 32%, var(--eq-sky) 44%, var(--eq-mint) 54%, var(--eq-green) 68%, var(--eq-yellow) 86%, var(--eq-orange) 100%);
    opacity: 0.9;
  }
</style>
</head>
<body>
  <main class="book-cover">
    <div class="equalizer" role="img" aria-label="Glowing rainbow audio equalizer bars with a soft reflection"></div>
    <svg class="cover-type" viewBox="0 0 731 1096" xmlns="http://www.w3.org/2000/svg">
      <text class="title" x="365.5" y="189" text-anchor="middle" font-size="196" textLength="650" lengthAdjust="spacingAndGlyphs">SCORING UP</text>
      <text class="subtitle" x="365.5" y="252" text-anchor="middle" font-size="60" textLength="648" lengthAdjust="spacingAndGlyphs">WINNING THROUGH THE NEW AGE</text>
      <text class="subtitle" x="365.5" y="306" text-anchor="middle" font-size="60" textLength="400" lengthAdjust="spacingAndGlyphs">OF JINGLE WORK</text>
      <text class="author" x="365.5" y="1052" text-anchor="middle" font-size="52" textLength="620" lengthAdjust="spacingAndGlyphs">Marco Vandesteen</text>
    </svg>
  </main>
</body>
</html>
```